Business card design for industrial spray painting - startup business

Design the layout of our new business card using the logo we have provided.

We want the card to be matt black in colour.

We only want our logo and slogan on the face side.

Because the card is black we would like the slogan WE PAINT ANYTHING! to be in white.

We want our information on the rear side.

I would like my name in blue matching the blue in the logo.

The remainder of the information should be in grey to match the grey in the logo.

The overall finish should look minimal, clean and slick.

Our business is industrlal and of a masculine nature.

Target Market(s)

industrial and mining companies

Contact Information for Business Card

(front of card – matt black)
insert logo here:
insert this tag line: WE PAINT ANYTHING!

--------------------------------------------------------------------------------------------------------------

(back of card – matt black)
Dorian Pelkey
Paint and Coatings Specialist
47 Holloway Crescent, Kenwick WA 6107
M: +61 431 872 914
T: +61 8 555 7136
E: dorian@gleamcoat.co
W: www.gleamcoat.co

Font styles to use
Sans Serif

Colors
000000
0455a3

Requirements
Must have
• clean, slick minimalist look. Masculine as we deal mostly with industrial spray painting

```html
<!DOCTYPE html>
<html lang="en">
<head>
<meta charset="utf-8">
<title>Gleam Coat – Business Card</title>
<link rel="stylesheet" href="https://fonts.googleapis.com/css2?family=Michroma&family=Roboto:wght@400;500;700&display=swap">
<style>
  :root {
    --backdrop: #1c1c1e;
    --card-black: #050505;
    --brand-blue: #1f7ccf;
    --brand-grey: #8d8f92;
    --divider-grey: #5e6064;
    --tagline-white: #ffffff;
  }
  * { box-sizing: border-box; margin: 0; padding: 0; }
  html, body {
    width: 1200px;
    height: 1200px;
    overflow: hidden;
    background: var(--backdrop);
  }
  .sheet {
    width: 1200px;
    height: 1200px;
    display: flex;
    flex-direction: column;
    align-items: center;
    justify-content: center;
    gap: 46px;
  }
  .card {
    width: 900px;
    height: 514px;
    background: var(--card-black);
    position: relative;
    box-shadow: 0 18px 40px rgba(0, 0, 0, 0.55);
  }

  /* Front */
  .card-front {
    display: flex;
    flex-direction: column;
    align-items: center;
    justify-content: center;
  }
  .brand {
    display: flex;
    align-items: center;
    gap: 22px;
  }
  .brand-dot {
    width: 26px;
    height: 26px;
    border-radius: 50%;
    background: var(--brand-blue);
  }
  .brand-name {
    font-family: "Michroma", sans-serif;
    font-size: 46px;
    letter-spacing: 2px;
    color: var(--brand-blue);
  }
  .tagline {
    margin-top: 92px;
    font-family: "Michroma", sans-serif;
    font-size: 17px;
    letter-spacing: 1.5px;
    color: var(--tagline-white);
  }

  /* Back */
  .card-back {
    display: flex;
    align-items: center;
    justify-content: center;
  }
  .person {
    width: 330px;
    text-align: right;
    padding-right: 42px;
    margin-top: -70px;
  }
  .person-name {
    font-family: "Roboto", sans-serif;
    font-weight: 700;
    font-size: 34px;
    color: var(--brand-blue);
    line-height: 1.05;
  }
  .person-role {
    font-family: "Roboto", sans-serif;
    font-size: 22px;
    color: var(--brand-grey);
    margin-top: 2px;
  }
  .divider {
    width: 2px;
    height: 184px;
    background: var(--divider-grey);
  }
  .contacts {
    width: 380px;
    padding-left: 46px;
    list-style: none;
    display: flex;
    flex-direction: column;
    gap: 18px;
  }
  .contact-row {
    display: flex;
    align-items: center;
    gap: 22px;
  }
  .contact-icon {
    flex: none;
    width: 44px;
    height: 44px;
    border-radius: 50%;
    background: var(--brand-blue);
    display: flex;
    align-items: center;
    justify-content: center;
  }
  .contact-text {
    font-family: "Roboto", sans-serif;
    font-size: 21px;
    line-height: 1.3;
    color: var(--brand-grey);
    letter-spacing: 0.5px;
  }
</style>
</head>
<body>
<main class="sheet">
  <section class="card card-front" aria-label="Card front">
    <div class="brand">
      <span class="brand-dot"></span>
      <span class="brand-name">GLEAM COAT</span>
    </div>
    <p class="tagline">WE PAINT ANYTHING!</p>
  </section>

  <section class="card card-back" aria-label="Card back">
    <div class="person">
      <h1 class="person-name">Dorian Pelkey</h1>
      <p class="person-role">Paint and Coatings Specialist</p>
    </div>
    <div class="divider"></div>
    <ul class="contacts">
      <li class="contact-row">
        <span class="contact-icon">
          <svg width="22" height="22" viewBox="0 0 24 24" aria-hidden="true">
            <path fill="#0a0a0a" d="M6.6 10.8a15.1 15.1 0 0 0 6.6 6.6l2.2-2.2a1 1 0 0 1 1-.25 11.4 11.4 0 0 0 3.6.57 1 1 0 0 1 1 1V20a1 1 0 0 1-1 1A17 17 0 0 1 3 4a1 1 0 0 1 1-1h3.5a1 1 0 0 1 1 1c0 1.25.2 2.45.57 3.57a1 1 0 0 1-.25 1z"/>
          </svg>
        </span>
        <p class="contact-text">M: +61 431 872 914<br>P: +61 8 555 7136</p>
      </li>
      <li class="contact-row">
        <span class="contact-icon">
          <svg width="26" height="26" viewBox="0 0 24 24" aria-hidden="true" fill="none" stroke="#0a0a0a" stroke-width="1.4">
            <circle cx="12" cy="12" r="9"/>
            <ellipse cx="12" cy="12" rx="4" ry="9"/>
            <line x1="3" y1="12" x2="21" y2="12"/>
            <line x1="4.5" y1="7.5" x2="19.5" y2="7.5"/>
            <line x1="4.5" y1="16.5" x2="19.5" y2="16.5"/>
          </svg>
        </span>
        <p class="contact-text">dorian@gleamcoat.co<br>www.gleamcoat.co</p>
      </li>
      <li class="contact-row">
        <span class="contact-icon">
          <svg width="22" height="22" viewBox="0 0 24 24" aria-hidden="true">
            <path fill="#0a0a0a" d="M12 2a7 7 0 0 0-7 7c0 5.2 7 13 7 13s7-7.8 7-13a7 7 0 0 0-7-7zm0 9.5A2.5 2.5 0 1 1 12 6.5a2.5 2.5 0 0 1 0 5z"/>
          </svg>
        </span>
        <p class="contact-text">47 Holloway Crescent<br>Kenwick WA 6107</p>
      </li>
    </ul>
  </section>
</main>
</body>
</html>
```